Now Leasing Banner

Looking for a banner that says the following information approx 4' x 30'

Now Leasing Maplewood Terrace 925-318-6054

Target Market(s)

Drive by traffic

Industry/Entity Type

Residential property management

Requirements
Must have
• Clear and readable from a distance

```html
<!DOCTYPE html>
<html lang="en">
<head>
<meta charset="utf-8">
<title>Now Leasing Maplewood Terrace</title>
<link rel="stylesheet" href="https://fonts.googleapis.com/css2?family=Montserrat:wght@600;700&display=swap">
<style>
  :root {
    --navy: #14254f;
    --accent-blue: #3f7fc4;
    --white: #ffffff;
    --photo-sky: #4f8fd6;
    --photo-building: #d8c7a8;
    --photo-foliage: #3f6a3a;
  }
  html, body {
    margin: 0;
    padding: 0;
    width: 1200px;
    height: 224px;
    overflow: hidden;
    background: var(--white);
  }
  .banner {
    position: absolute;
    left: 62px;
    top: 31px;
    width: 1102px;
    height: 162px;
    overflow: hidden;
    box-shadow: 0 0 0 1px #e4e6ea;
  }
  .banner-shapes {
    position: absolute;
    inset: 0;
  }
  .property-photo {
    position: absolute;
    left: 0;
    top: 0;
  }
  .message {
    position: absolute;
    left: 0;
    top: 0;
    width: 620px;
    height: 162px;
    display: flex;
    flex-direction: column;
    align-items: center;
    justify-content: center;
    gap: 6px;
    color: var(--white);
    font-family: "Montserrat", sans-serif;
  }
  .headline {
    margin: 0;
    font-size: 32px;
    font-weight: 700;
    letter-spacing: 0.2px;
    white-space: nowrap;
  }
  .phone {
    display: flex;
    align-items: center;
    gap: 16px;
    font-size: 34px;
    font-weight: 700;
    letter-spacing: 0.5px;
  }
  .phone-icon {
    width: 36px;
    height: 36px;
  }
</style>
</head>
<body>
  <div class="banner">
    <svg class="banner-shapes" width="1102" height="162" viewBox="0 0 1102 162">
      <defs>
        <linearGradient id="photoTone" x1="0" y1="0" x2="0" y2="1">
          <stop offset="0" stop-color="var(--photo-sky)"/>
          <stop offset="0.45" stop-color="#9fbfe0"/>
          <stop offset="0.6" stop-color="var(--photo-building)"/>
          <stop offset="1" stop-color="#b9a888"/>
        </linearGradient>
      </defs>
      <rect class="property-photo" x="560" y="0" width="542" height="162" fill="url(#photoTone)" role="img" aria-label="Photo of two-storey apartment buildings with tile roofs, balconies and trees under a blue sky"/>
      <polygon class="accent-stripe" points="0,0 650,0 594,162 0,162" fill="var(--accent-blue)"/>
      <polygon class="navy-panel" points="0,0 638,0 582,162 0,162" fill="var(--navy)"/>
    </svg>
    <div class="message">
      <h1 class="headline">Now Leasing Maplewood Terrace</h1>
      <div class="phone">
        <svg class="phone-icon" viewBox="0 0 24 24" aria-hidden="true">
          <path fill="var(--white)" d="M6.6 2.5c.5-.3 1.1-.2 1.4.3l2 3.2c.3.5.2 1.1-.2 1.5L8.3 8.8c.9 2.6 3 4.7 5.6 5.6l1.3-1.5c.4-.4 1-.5 1.5-.2l3.2 2c.5.3.6.9.3 1.4l-1.3 2.3c-.4.7-1.2 1.1-2 1-7-.8-12.5-6.3-13.3-13.3-.1-.8.3-1.6 1-2z"/>
          <path fill="none" stroke="var(--white)" stroke-width="1.6" stroke-linecap="round" d="M14 3.5a6.5 6.5 0 0 1 6.5 6.5M14 7a3 3 0 0 1 3 3"/>
        </svg>
        <span class="phone-number">925-318-6054</span>
      </div>
    </div>
  </div>
</body>
</html>
```